Design logo and business card.

Design and construct logo and card for my business which is an over seeing company of other smaller businesses. The companies name is quarry5 business collective. Im open to any ideas but i am looking for a very cool contemporary design with a very prestige feel. The card can be either single or double sided, Thank you and i will look forward to your submissions.

Industry/Entity Type

Business

Requirements
Must have
• Company name, email, website, telephone, my name. Cool modern look with a prestige feel.

```html
<!DOCTYPE html>
<html lang="en">
<head>
<meta charset="utf-8">
<title>Quarry5 Business Collective – Business Card</title>
<link rel="stylesheet" href="https://fonts.googleapis.com/css2?family=Quicksand:wght@700&display=swap">
<style>
  :root {
    --leaf-green: #8cc04a;
    --fresh-green: #a9cf4f;
    --lime-light: #d6e67a;
    --cream-yellow: #f5ee9a;
    --sun-yellow: #f3c93a;
    --brand-brown: #4a1a16;
    --contact-white: #ffffff;
  }
  html, body {
    margin: 0;
    padding: 0;
    width: 1200px;
    height: 686px;
    overflow: hidden;
    background: #ffffff;
  }
  .business-card {
    position: relative;
    width: 1200px;
    height: 686px;
    overflow: hidden;
    font-family: "Quicksand", sans-serif;
  }
  .floral-background {
    position: absolute;
    inset: 0;
    width: 100%;
    height: 100%;
  }
  .brand-name {
    position: absolute;
    left: 314px;
    top: 250px;
    width: 836px;
    margin: 0;
    text-align: center;
    font-size: 200px;
    font-weight: 700;
    line-height: 1;
    color: var(--brand-brown);
  }
  .contact-details {
    position: absolute;
    left: 23px;
    top: 527px;
    margin: 0;
    padding: 0;
    list-style: none;
    font-size: 27px;
    font-weight: 700;
    line-height: 35.5px;
    letter-spacing: 0.5px;
    color: var(--contact-white);
  }
</style>
</head>
<body>
  <main class="business-card">
    <svg class="floral-background" role="img" aria-label="Decorative pattern of stylised green leaves and yellow flowers on a light yellow-green ground" viewBox="0 0 1200 686" preserveAspectRatio="none">
      <defs>
        <radialGradient id="background-glow" cx="0.5" cy="0.3" r="0.75">
          <stop offset="0" stop-color="var(--cream-yellow)"/>
          <stop offset="0.45" stop-color="var(--lime-light)"/>
          <stop offset="1" stop-color="var(--fresh-green)"/>
        </radialGradient>
        <linearGradient id="background-depth" x1="0" y1="0" x2="1" y2="1">
          <stop offset="0" stop-color="var(--leaf-green)" stop-opacity="0.35"/>
          <stop offset="0.5" stop-color="var(--sun-yellow)" stop-opacity="0.12"/>
          <stop offset="1" stop-color="var(--leaf-green)" stop-opacity="0.4"/>
        </linearGradient>
      </defs>
      <rect width="1200" height="686" fill="url(#background-glow)"/>
      <rect width="1200" height="686" fill="url(#background-depth)"/>
    </svg>

    <h1 class="brand-name">Quarry5</h1>

    <ul class="contact-details">
      <li>Website quarry-5.com</li>
      <li>Email info@quarry-5.com</li>
      <li>Name kit ross</li>
      <li>Tel. +34 611 482 907</li>
    </ul>
  </main>
</body>
</html>
```